Business Cards

Need a neat design for a new business card

Industry/Entity Type

Residential Construction

Contact Information for Business Card

Company Name- KOVE Construction Inc.
Owner- Marcus Tolliver
Phone number- (555)203-7481
Email- kovecohomes@brindlemail.example
Facebook- www.socialpage.example/kovecohomes

Colors
fefdec

```html
<!DOCTYPE html>
<html lang="en">
<head>
<meta charset="utf-8">
<title>KOVE Construction – Business Card</title>
<link rel="stylesheet" href="https://fonts.googleapis.com/css2?family=Cinzel:wght@400&family=Montserrat:wght@400;500&display=swap">
<style>
  :root {
    --backdrop: #2a2a2a;
    --card: #0b0b0b;
    --ink: #f2f2f2;
    --silver: #b9b9b9;
    --cream: #fefdec;
    --rule: #d8d8d8;
  }
  * { margin: 0; padding: 0; box-sizing: border-box; }
  html, body { width: 1200px; height: 900px; overflow: hidden; }
  body {
    background: var(--backdrop);
    font-family: "Montserrat", sans-serif;
    color: var(--ink);
    position: relative;
  }
  .card {
    position: absolute;
    left: 250px;
    width: 700px;
    height: 400px;
    background: var(--card);
    overflow: hidden;
  }
  .card--front { top: 35px; }
  .card--back { top: 465px; }

  /* Front */
  .front-mark {
    position: absolute;
    inset: 0;
    display: flex;
    align-items: center;
    justify-content: center;
    gap: 22px;
  }
  .front-mark__square {
    width: 26px; height: 26px;
    background: var(--silver);
  }
  .front-mark__name {
    font-family: "Montserrat", sans-serif;
    font-weight: 500;
    font-size: 40px;
    letter-spacing: 8px;
    color: var(--silver);
    text-transform: uppercase;
    line-height: 1;
  }

  /* Back */
  .brand {
    position: absolute;
    top: 70px;
    right: 60px;
    display: flex;
    align-items: center;
    gap: 14px;
  }
  .brand__square { width: 18px; height: 18px; background: var(--ink); }
  .brand__name {
    font-family: "Montserrat", sans-serif;
    font-weight: 500;
    font-size: 24px;
    letter-spacing: 4px;
    color: var(--ink);
    text-transform: uppercase;
  }
  .person {
    position: absolute;
    left: 60px;
    top: 170px;
  }
  .person__name {
    font-family: "Cinzel", serif;
    font-size: 30px;
    line-height: 1;
    letter-spacing: 1px;
  }
  .person__role {
    font-family: "Cinzel", serif;
    font-size: 15px;
    margin-top: 4px;
    letter-spacing: 1px;
  }
  .divider {
    position: absolute;
    left: 60px;
    right: 60px;
    top: 240px;
    height: 1px;
    background: var(--rule);
  }
  .contacts {
    position: absolute;
    left: 60px;
    top: 254px;
    list-style: none;
    font-size: 16px;
    line-height: 28px;
  }
  .contacts li { display: flex; align-items: center; gap: 10px; white-space: nowrap; }
  .contacts svg { width: 16px; height: 16px; flex: none; }
  .social {
    position: absolute;
    right: 60px;
    top: 324px;
    display: flex;
    align-items: center;
    gap: 10px;
    font-size: 16px;
    line-height: 24px;
    white-space: nowrap;
  }
  .social__dot { width: 16px; height: 16px; border-radius: 50%; background: var(--ink); }
  .footer-band { position: absolute; left: 0; bottom: 0; width: 700px; height: 40px; }
</style>
</head>
<body>
  <section class="card card--front" aria-label="Card front">
    <div class="front-mark">
      <span class="front-mark__square"></span>
      <span class="front-mark__name">KOVE Construction</span>
    </div>
  </section>

  <section class="card card--back" aria-label="Card back">
    <div class="brand">
      <span class="brand__square"></span>
      <span class="brand__name">KOVE Construction</span>
    </div>

    <div class="person">
      <p class="person__name">Marcus Tolliver</p>
      <p class="person__role">Owner</p>
    </div>

    <div class="divider"></div>

    <ul class="contacts">
      <li>
        <svg viewBox="0 0 24 24" fill="none" stroke="currentColor" stroke-width="2" stroke-linecap="round" stroke-linejoin="round"><path d="M22 16.9v3a2 2 0 0 1-2.2 2 19.8 19.8 0 0 1-8.6-3.1 19.5 19.5 0 0 1-6-6A19.8 19.8 0 0 1 2.1 4.2 2 2 0 0 1 4.1 2h3a2 2 0 0 1 2 1.7c.1.9.4 1.8.7 2.7a2 2 0 0 1-.5 2.1L8 9.8a16 16 0 0 0 6 6l1.3-1.3a2 2 0 0 1 2.1-.4c.9.3 1.8.6 2.7.7a2 2 0 0 1 1.7 2z"/></svg>
        (555) 203-7481
      </li>
      <li>
        <svg viewBox="0 0 24 24" fill="none" stroke="currentColor" stroke-width="2" stroke-linejoin="round"><rect x="2" y="5" width="20" height="14"/><path d="M2 5l10 8 10-8"/></svg>
        kovecohomes@brindlemail.example
      </li>
    </ul>

    <div class="social">
      <span>socialpage.example/kovecohomes</span>
      <span class="social__dot"></span>
    </div>

    <svg class="footer-band" viewBox="0 0 700 40" preserveAspectRatio="none" aria-hidden="true">
      <polygon points="0,10 300,18 312,34 700,28 700,40 0,40" fill="var(--cream)"/>
      <polygon points="300,18 308,18 322,30 312,34" fill="var(--card)"/>
    </svg>
  </section>
</body>
</html>
```